Design a business Card

Design a business card (front and back) for a Technology Consulting firm. Preference is for a clean look - professional, favour minimalist rather than something busy. two logos are attached. You can use any of them. . The information below is for the purpose of presenting an entry in the contest, but the winner will be given correct information to product another version of the entry. The winner will also be given an opportunity to prepare a letterhead (ideally consistent with the business card).

Carla Wendover
Partner
+61 438 926 417
+61 7 3890 2615
jane@[url removed, login to view]
[url removed, login to view]
GPO Box 6093
Brisbane QLD 4009

The winning entry should be in a format that most business card printers can easily print.

```html
<!DOCTYPE html>
<html lang="en">
<head>
<meta charset="utf-8">
<title>Brellan Consulting – Business Card</title>
<link rel="stylesheet" href="https://fonts.googleapis.com/css2?family=Quicksand:wght@500;700&family=Open+Sans:wght@400;600&display=swap">
<style>
  :root {
    --backdrop: #e8e9ec;
    --card: #ffffff;
    --brand-blue: #1f86c8;
    --ink: #4a4d52;
    --ink-soft: #7b7f86;
    --rule: #1f86c8;
  }
  * { box-sizing: border-box; margin: 0; padding: 0; }
  html, body { width: 1200px; height: 900px; overflow: hidden; }
  body {
    background: var(--backdrop);
    position: relative;
    font-family: "Open Sans", sans-serif;
    color: var(--ink);
  }
  .card {
    position: absolute;
    width: 560px;
    height: 320px;
    background: var(--card);
    border-radius: 22px;
    overflow: hidden;
    box-shadow: 0 10px 28px rgba(0,0,0,0.12);
  }
  .card--back { left: 580px; top: 110px; }
  .card--front { left: 60px; top: 470px; }

  .brand {
    display: flex;
    align-items: center;
    gap: 10px;
    font-family: "Quicksand", sans-serif;
    font-weight: 700;
    color: var(--brand-blue);
  }
  .brand__mark { background: var(--brand-blue); flex: none; }

  .card--back .brand {
    position: absolute; left: 60px; top: 112px; font-size: 26px;
  }
  .card--back .brand__mark { width: 26px; height: 26px; }
  .card--back .website {
    position: absolute; left: 96px; top: 186px;
    font-size: 14px; color: var(--brand-blue); letter-spacing: 0.3px;
  }

  .card--front .brand {
    position: absolute; left: 40px; top: 46px; font-size: 17px;
  }
  .card--front .brand__mark { width: 17px; height: 17px; }

  .person { position: absolute; left: 260px; top: 104px; }
  .person__name {
    font-family: "Quicksand", sans-serif; font-weight: 700;
    font-size: 26px; color: var(--brand-blue);
  }
  .person__title { font-size: 13px; color: var(--ink-soft); margin-top: 2px; }

  .contacts {
    position: absolute; left: 216px; top: 174px;
    border-left: 2px solid var(--rule);
    padding-left: 14px;
    list-style: none;
  }
  .contacts li {
    display: flex; align-items: center; gap: 10px;
    font-size: 13.5px; line-height: 22px; color: var(--ink);
  }
  .contacts svg { width: 14px; height: 14px; flex: none; }
  .address { display: block; line-height: 20px; }

  .accent-band {
    position: absolute; left: 0; bottom: 0;
    width: 190px; height: 12px; background: var(--brand-blue);
  }
</style>
</head>
<body>

  <section class="card card--back" aria-label="Card back">
    <div class="brand"><span class="brand__mark"></span>Brellan Consulting Services Ltd</div>
    <p class="website">www.brellanworth.com</p>
  </section>

  <section class="card card--front" aria-label="Card front">
    <div class="brand"><span class="brand__mark"></span>Brellan Consulting Services Ltd</div>

    <div class="person">
      <h1 class="person__name">Carla Wendover</h1>
      <p class="person__title">Head Honcho</p>
    </div>

    <ul class="contacts">
      <li>
        <svg viewBox="0 0 16 16" aria-hidden="true"><path d="M4 1.5h2.2l1 3.2-1.6 1.2a8 8 0 0 0 4.5 4.5l1.2-1.6 3.2 1V12a2.5 2.5 0 0 1-2.5 2.5A11.5 11.5 0 0 1 1.5 4 2.5 2.5 0 0 1 4 1.5z" fill="none" stroke="#4a4d52" stroke-width="1.3"/></svg>
        +61 438 926 417
      </li>
      <li>
        <svg viewBox="0 0 16 16" aria-hidden="true"><rect x="2" y="2" width="12" height="12" rx="1.5" fill="none" stroke="#4a4d52" stroke-width="1.3"/></svg>
        +61 7 3890 2615
      </li>
      <li>
        <svg viewBox="0 0 16 16" aria-hidden="true"><rect x="1.5" y="3.5" width="13" height="9" fill="none" stroke="#4a4d52" stroke-width="1.3"/><path d="M1.5 3.5 8 9l6.5-5.5" fill="none" stroke="#4a4d52" stroke-width="1.3"/></svg>
        carla@brellanworth.com
      </li>
      <li>
        <svg viewBox="0 0 16 16" aria-hidden="true"><circle cx="8" cy="8" r="6.3" fill="none" stroke="#4a4d52" stroke-width="1.3"/><ellipse cx="8" cy="8" rx="2.8" ry="6.3" fill="none" stroke="#4a4d52" stroke-width="1.1"/><path d="M1.7 8h12.6" stroke="#4a4d52" stroke-width="1.1"/></svg>
        www.brellanworth.com
      </li>
      <li>
        <svg viewBox="0 0 16 16" aria-hidden="true"><path d="M8 15s5-5 5-9a5 5 0 0 0-10 0c0 4 5 9 5 9z" fill="none" stroke="#4a4d52" stroke-width="1.3"/><circle cx="8" cy="6" r="1.8" fill="#4a4d52"/></svg>
        <span class="address">GPO Box 6093<br>Brisbane QLD 4009</span>
      </li>
    </ul>

    <div class="accent-band"></div>
  </section>

</body>
</html>
```